Brightmoor Cleaning Services

need a brochure for my cleaning company. Contact info coming soon .

Target Market(s)

Cleaning Services

Industry/Entity Type

Cleaning Service

Requirements
Must have
• I attached logo for you to use.

Corporate address -
472 Kestrel Ridge W Ste 518
Larkfield, OR 97102

Phone number - 877-514-SHINE
Nice to have
• bifold brochure. I attached some samples
Should not have
• Pictures of people. Keep it clean and professional.

```html
<!DOCTYPE html>
<html lang="en">
<head>
<meta charset="utf-8">
<title>Brightmoor Cleaning Services – Trifold Brochure</title>
<link href="https://fonts.googleapis.com/css2?family=Montserrat:wght@400;500;700;800&display=swap" rel="stylesheet">
<style>
:root{
  --blue:#0a6fc0;
  --blue-text:#1565b8;
  --red:#e8202a;
  --white:#ffffff;
  --ink:#3a3f47;
}
*{margin:0;padding:0;box-sizing:border-box}
html,body{width:1200px;height:940px;overflow:hidden;background:var(--blue)}
body{font-family:'Montserrat',sans-serif;color:var(--white)}
.brochure{position:relative;width:1200px;height:940px;background:var(--blue);overflow:hidden}
.fold{position:absolute;top:0;width:6px;height:940px;background:linear-gradient(90deg,rgba(0,0,0,.06),rgba(0,0,0,0))}
.fold--one{left:398px}.fold--two{left:798px}
.backdrop{position:absolute;inset:0}
.photo{position:absolute;border-radius:50%;border:10px solid var(--red)}
.photo--spray{left:-22px;top:258px;width:234px;height:234px;background:radial-gradient(circle at 40% 45%,#f3c45a,#c98d3a 55%,#7c8a5a)}
.photo--cart{left:226px;top:306px;width:160px;height:160px;background:radial-gradient(circle at 50% 55%,#e6c24a,#9aa3ad 60%,#7b8590)}
.photo--carpet{left:433px;top:275px;width:220px;height:220px;background:radial-gradient(circle at 55% 60%,#e9dcc2,#cbb894 60%,#a69372)}
.photo--glove{left:659px;top:467px;width:220px;height:220px;background:radial-gradient(circle at 45% 50%,#f3e3a3,#b9c4d6 55%,#8494b0)}
.photo--bucket{left:938px;top:565px;width:176px;height:176px;background:radial-gradient(circle at 45% 55%,#e2453c,#5a8fd6 50%,#9a9a98)}
.line{display:block;white-space:nowrap;text-align:justify;text-align-last:justify}
.line--end{text-align-last:left}
.about{position:absolute;left:34px;top:50px;width:316px}
.about__title{font-size:40px;font-weight:800;line-height:40px;letter-spacing:-.3px}
.about__text{margin-top:24px;font-size:13.4px;line-height:18.4px;font-weight:400}
.service{position:absolute;left:28px;width:330px;list-style:none}
.service--res{top:521px}.service--com{top:609px}.service--eco{top:711px}.service--sch{top:799px}
.service__icon{position:absolute;left:0;top:0;width:60px;height:52px}
.service__body{position:absolute;left:75px;top:0;width:251px}
.service__name{font-size:14.2px;font-weight:700;line-height:16px}
.service__text{font-size:12.2px;line-height:16.3px;letter-spacing:.3px}
.rule{position:absolute;height:2px;background:var(--red)}
.rule--left{left:17px;top:885px;width:357px}
.rule--right{left:828px;top:885px;width:356px}
.web{position:absolute;top:897px;font-size:15px;letter-spacing:3.4px;text-align:center}
.web--left{left:17px;width:357px}
.web--right{left:828px;width:356px}
.quote{position:absolute;left:560px;top:30px;width:210px;text-align:right;color:var(--ink)}
.quote__mark{font-size:50px;font-weight:800;color:var(--blue-text);line-height:36px;height:30px}
.quote__text{margin-top:12px;font-size:16.2px;line-height:20.9px;font-weight:400;white-space:nowrap}
.quote__author{margin-top:6px;font-size:16.5px;font-weight:700;color:var(--blue-text)}
.brand{position:absolute;display:flex;align-items:center;gap:10px;font-weight:800;line-height:1.05}
.brand__dot{flex:none;border-radius:50%;width:26px;height:26px}
.brand--top{left:898px;top:48px;width:220px;color:var(--blue-text);font-size:22px}
.brand--top .brand__dot{background:var(--blue-text)}
.brand--mid{left:453px;top:698px;width:230px;color:var(--white);font-size:22px}
.brand--mid .brand__dot{background:var(--white)}
.contact{position:absolute;left:453px;top:804px;font-style:normal}
.contact__address{font-size:17.5px;line-height:21px;font-weight:400}
.contact__phone{margin-top:20px;font-size:22px;font-weight:700;line-height:24px}
.contact__web{font-size:16.5px;line-height:20px}
.cover{position:absolute;left:828px;top:766px;width:360px}
.cover__kicker{font-size:20.5px;font-weight:400;line-height:24px;white-space:nowrap}
.cover__title{font-size:42.5px;font-weight:800;line-height:44px;margin-top:2px;white-space:nowrap}
.cover__title span{display:block;font-size:34.5px;line-height:40px}
</style>
</head>
<body>
<main class="brochure">
  <svg class="backdrop" width="1200" height="940" viewBox="0 0 1200 940" role="img" aria-label="Photo of a blue bucket filled with cleaning bottles and sponges on a bright kitchen counter">
    <defs>
      <linearGradient id="kitchen" x1="0" y1="0" x2="1" y2="1">
        <stop offset="0" stop-color="#f6f5f1"/>
        <stop offset=".45" stop-color="#ece7dc"/>
        <stop offset=".75" stop-color="#c9d7e8"/>
        <stop offset="1" stop-color="#9bbde6"/>
      </linearGradient>
    </defs>
    <path d="M445,0 C500,200 620,380 800,520 C930,615 1050,680 1200,715 L1200,0 Z" fill="url(#kitchen)"/>
    <path d="M445,0 C500,200 620,380 800,520 C930,615 1050,680 1200,715" fill="none" stroke="#ffffff" stroke-width="26"/>
  </svg>
  <div class="fold fold--one"></div>
  <div class="fold fold--two"></div>

  <section class="about">
    <h1 class="about__title">About Us</h1>
    <p class="about__text">
      <span class="line">Lorem ipsum dolor sit amet, consectetuer</span>
      <span class="line">adipiscing elit, sed diam nonummy nibh eu-</span>
      <span class="line">ismod tincidunt ut laoreet dolore magna</span>
      <span class="line">aliquam erat volutpat. Ut wisi enim ad</span>
      <span class="line">minim veniam, quis nostrud exerci tation ul-</span>
      <span class="line">lamcorper suscipit lobortis nisl ut aliquip ex</span>
      <span class="line line--end">ea commodo consequat.</span>
    </p>
  </section>

  <div class="photo photo--spray" role="img" aria-label="Photo of a spray bottle and yellow sponge cleaning a surface"></div>
  <div class="photo photo--cart" role="img" aria-label="Photo of a janitorial cart with mop and cloths"></div>
  <div class="photo photo--carpet" role="img" aria-label="Photo of a vacuum head on a beige carpet"></div>
  <div class="photo photo--glove" role="img" aria-label="Photo of a gloved hand wiping a tap with a blue sponge"></div>
  <div class="photo photo--bucket" role="img" aria-label="Photo of a red bucket with gloves, bottles and a mop"></div>

  <ul class="services">
    <li class="service service--res">
      <svg class="service__icon" viewBox="0 0 62 52" fill="none" stroke="#fff" stroke-width="2.4"><path d="M2 50H60M6 50V18L14 2H38L44 18V50M4 18H44M44 30H58V50M18 22h12v24H18zM18 30h12M18 38h12M24 22v24M50 42v6M54 42v6"/></svg>
      <div class="service__body">
        <h2 class="service__name">RESIDENTIAL</h2>
        <p class="service__text"><span class="line">Lorem ipsum dolor sit amet, consec-</span><span class="line">tetuer adipiscing elit, sed diam nonum-</span><span class="line">my nibh euismod tincidunt ut laoreet</span></p>
      </div>
    </li>
    <li class="service service--com">
      <svg class="service__icon" viewBox="0 0 62 56" fill="none" stroke="#fff" stroke-width="2.4"><path d="M2 54H60M6 54V8H30V54M30 20H56V54M14 8V2h8v6M11 16h5v5h-5zM20 16h5v5h-5zM11 27h5v5h-5zM20 27h5v5h-5zM11 38h5v5h-5zM20 38h5v5h-5zM35 28h6v6h-6zM46 28h6v6h-6zM35 40h6v6h-6zM46 40h6v6h-6zM14 54v-8h6v8"/></svg>
      <div class="service__body">
        <h2 class="service__name">COMMERCIAL</h2>
        <p class="service__text"><span class="line">Ut wisi enim ad minim veniam, quis</span><span class="line">nostrud exerci tation ullamcorper sus-</span><span class="line">cipit lobortis nisl ut aliquip ex ea com-</span></p>
      </div>
    </li>
    <li class="service service--eco">
      <svg class="service__icon" viewBox="0 0 64 56" fill="none" stroke="#fff" stroke-width="2.4"><circle cx="32" cy="24" r="20"/><path d="M12 24H52M32 4c-8 6-8 34 0 40M32 4c8 6 8 34 0 40M16 12H48M16 36H48M2 36c10-4 22 0 28 16C18 56 6 50 2 36zM62 36c-10-4-22 0-28 16 12 4 24-2 28-16z"/></svg>
      <div class="service__body">
        <h2 class="service__name">ECO ATMOSPHERE</h2>
        <p class="service__text"><span class="line">Lorem ipsum dolor sit amet, consec-</span><span class="line">tetuer adipiscing elit, sed diam nonum-</span><span class="line">my nibh euismod tincidunt ut laoreet</span></p>
      </div>
    </li>
    <li class="service service--sch">
      <svg class="service__icon" viewBox="0 0 62 56" fill="none" stroke="#fff" stroke-width="2.4"><path d="M36 44H4V8H50V24M4 18H50M14 2v10M40 2v10M10 26h10M10 32h14M10 38h10"/><circle cx="48" cy="42" r="12"/><path d="M48 35v7l5 3"/></svg>
      <div class="service__body">
        <h2 class="service__name">SCHEDULE US</h2>
        <p class="service__text"><span class="line">Ut wisi enim ad minim veniam, quis</span><span class="line">nostrud exerci tation ullamcorper sus-</span><span class="line">cipit lobortis nisl ut aliquip ex ea com-</span></p>
      </div>
    </li>
  </ul>

  <div class="rule rule--left"></div>
  <p class="web web--left">www.brightmoorclean.com</p>

  <blockquote class="quote">
    <div class="quote__mark">“”</div>
    <p class="quote__text">Lorem ipsum dolor sit<br>amet, consectetuer<br>adipiscing elit, sed<br>diam nonummy nibh<br>euismod tincidLorem<br>ipsum dolor sit amet,<br>consectetuer adipisc-<br>ing elit, sed diam<br>nonummy nibh euis-<br>mod tincid</p>
    <p class="quote__author">Lorem ipsum</p>
  </blockquote>

  <div class="brand brand--top"><span class="brand__dot"></span>Brightmoor Cleaning Services</div>
  <div class="brand brand--mid"><span class="brand__dot"></span>Brightmoor Cleaning Services</div>

  <address class="contact">
    <p class="contact__address">472 Kestrel Ridge W Ste 518<br>Larkfield, OR 97102</p>
    <p class="contact__phone">877-514-SHINE</p>
    <p class="contact__web">www.brightmoorclean.com</p>
  </address>

  <section class="cover">
    <p class="cover__kicker">RESIDENTIAL AND COMMERCIAL</p>
    <h2 class="cover__title">PROFESSIONAL<span>CLEANING SERVICE</span></h2>
  </section>

  <div class="rule rule--right"></div>
  <p class="web web--right">www.brightmoorclean.com</p>
</main>
</body>
</html>
```